Sydney law firm, Pelbury Solicitors, needs a flyer design!

We need a flyer design for our law firm which has been operating in Sydney for over 35 years. We want to send the flyer out to potential clients and also to existing clients to let them know the range of services that we provide. Our corporate colours are white, red and black and we would like these incorporated somewhat. The final design should be clean, modern and professional.

We would like the design to fit a double sided flyer approx. 210mm high x 100mm wide.

Law Firm

Serif
Sans Serif

eb2026
ffffff

• Details needed on the flyer are:
• Pelbury Solicitors
• 3/82 Tarrow Street, Liverpool, NSW 2170
• (02) 9413 5862
• www.pelburysolicitors-example.com.au
• info@pelburysolicitors-example.com.au
• Our areas of practice include:
• Property Law
• Conveyancing
• Leases
• Criminal Law
• Family Law
• Litigation and Dispute Resolution
• Company Law
• Wills and Estates
• Powers of Attorney and Guardianship
• a picture of scales or a picture of a gavel

```html
<!DOCTYPE html>
<html lang="en">
<head>
<meta charset="utf-8">
<title>Pelbury Solicitors – Flyer Options</title>
<link rel="stylesheet" href="https://fonts.googleapis.com/css2?family=Cinzel:wght@400&family=Fira+Sans+Extra+Condensed:wght@300;400;500&family=Open+Sans:wght@700&display=swap">
<style>
  :root{
    --red:#c4331f;
    --red-line:#c8321f;
    --ink:#1a1a1a;
    --text:#2b2b2b;
    --white:#ffffff;
    --silver-edge:#bfc0c1;
    --silver-mid:#e4e5e6;
    --footer-grey:#c9caca;
    --label:#333333;
  }
  *{box-sizing:border-box;margin:0;padding:0}
  html,body{width:1150px;height:1200px;overflow:hidden;background:var(--white)}
  body{position:relative;font-family:"Fira Sans Extra Condensed","Arial Narrow",sans-serif;color:var(--text)}

  .option-label{position:absolute;font:400 24px/1 Arial,sans-serif;color:var(--label)}

  .flyer{position:absolute;overflow:hidden}
  .flyer--silver{left:42px;top:83px;width:514px;height:1072px;
    background:linear-gradient(90deg,var(--silver-edge) 0%,var(--silver-mid) 25%,#fafafa 50%,var(--silver-mid) 75%,var(--silver-edge) 100%)}
  .flyer--white{left:600px;top:84px;width:509px;height:1076px;background:var(--white);border:1px solid #e6e6e6}
  .flyer--white .body-wash{position:absolute;left:0;right:0;top:296px;height:720px;
    background:radial-gradient(ellipse 60% 55% at 35% 45%,#c8c9ca 0%,#e6e7e8 45%,#ffffff 80%)}

  .wordmark{position:absolute;left:0;right:0;text-align:center;font-family:"Cinzel",Georgia,serif;font-weight:400;color:var(--ink)}
  .wordmark__name{display:block;font-size:70px;line-height:1;letter-spacing:1px}
  .wordmark__tag{display:block;font-size:22px;line-height:1;letter-spacing:17px;margin-top:10px;padding-left:17px}

  .web-band{position:absolute;left:0;right:0;height:36px;background:var(--red);color:var(--white);
    font:700 17px/36px "Open Sans",Arial,sans-serif;text-align:center;letter-spacing:0}

  .photo{position:absolute;left:0;right:0;height:340px;
    background:
      linear-gradient(180deg,rgba(255,255,255,0) 60%,rgba(230,230,230,.95) 100%),
      linear-gradient(90deg,#6b6b6a 0%,#3a3a3c 25%,#c9b29b 45%,#8d8f95 62%,#1d2230 80%,#2e3340 100%)}

  .intro{position:absolute;left:33px;width:455px;font-size:19px;line-height:25.7px;letter-spacing:-0.2px;font-weight:400;color:var(--text)}

  .practice{position:absolute;left:118px;font-size:19.5px;line-height:25.6px;color:var(--text)}
  .practice ul{list-style:none}
  .practice li{position:relative;padding-left:27px}
  .practice li::before{content:"";position:absolute;left:3px;top:10px;width:6px;height:6px;background:var(--red)}

  .contact{position:absolute;left:0;right:0;text-align:center;font-size:19.5px;line-height:26px}
  .contact svg{width:16px;height:14px;vertical-align:-1px;margin-right:6px}
  .flyer--silver .contact{color:var(--white)}
  .flyer--silver .contact .phone{font-weight:500}
  .flyer--white .contact{color:var(--text)}

  .footer{position:absolute;left:0;right:0;bottom:0}
  .flyer--silver .footer{height:130px;background:var(--red)}
  .flyer--silver .chrome-bar{position:absolute;left:0;right:0;top:932px;height:10px;
    background:linear-gradient(90deg,#bbb 0%,#555 10%,#eee 25%,#999 40%,#fff 55%,#777 70%,#ddd 85%,#444 100%)}
  .flyer--white .footer{height:125px;background:var(--footer-grey);border-top:5px solid var(--red-line)}
</style>
</head>
<body>

<span class="option-label" style="left:288px;top:46px">1</span>
<span class="option-label" style="left:842px;top:55px">2</span>

<section class="flyer flyer--silver">
  <div class="wordmark" style="top:62px">
    <span class="wordmark__name">PELBURY</span>
    <span class="wordmark__tag">SOLICITORS</span>
  </div>
  <div class="web-band" style="top:179px">WWW.PELBURYSOLICITORS-EXAMPLE.COM.AU</div>
  <div class="photo" role="img" aria-label="Photo of two professionals shaking hands across an office desk" style="top:215px"></div>
  <p class="intro" style="top:536px">Pelbury Solicitors is a private law firm based in Liverpool that has been servicing the Sydney area for over 30 years. With a dedicated, professional and friendly team we pride ourselves on delivering an exceptional legal service to our clients.</p>
  <div class="practice" style="top:659px">
    <p>Our areas of practice include:</p>
    <ul>
      <li>Property Law</li><li>Conveyancing</li><li>Leases</li><li>Criminal Law</li><li>Family Law</li>
      <li>Litigation and Dispute Resolution</li><li>Company Law</li><li>Wills and Estates</li>
      <li>Powers of Attorney and Guardianship</li>
    </ul>
  </div>
  <div class="chrome-bar"></div>
  <footer class="footer">
    <div class="contact" style="top:20px">
      <div><svg viewBox="0 0 16 14" fill="currentColor"><path d="M8 0 0 6h2v8h5V9h2v5h5V6h2z"/></svg>3/82 Tarrow Street, Liverpool, NSW 2170</div>
      <div class="phone"><svg viewBox="0 0 16 14" fill="currentColor" style="width:12px;margin-right:1px"><path d="M3 0h3l1 4-2 1q1 3 4 4l1-2 4 1v3q0 2-2 2Q2 12 1 2q0-2 2-2z"/></svg>(02) 9413 5862</div>
      <div><svg viewBox="0 0 16 14" fill="none" stroke="currentColor" stroke-width="1.4"><rect x="1" y="2" width="14" height="10"/><path d="m1 2 7 6 7-6"/></svg>info@pelburysolicitors-example.com.au</div>
    </div>
  </footer>
</section>

<section class="flyer flyer--white">
  <div class="body-wash"></div>
  <div class="wordmark" style="top:56px">
    <span class="wordmark__name">PELBURY</span>
    <span class="wordmark__tag">SOLICITORS</span>
  </div>
  <div class="web-band" style="top:177px">WWW.PELBURYSOLICITORS-EXAMPLE.COM.AU</div>
  <div class="photo" role="img" aria-label="Photo of two professionals shaking hands across an office desk" style="top:213px"></div>
  <p class="intro" style="top:533px;left:27px">Pelbury Solicitors is a private law firm based in Liverpool that has been servicing the Sydney area for over 30 years. With a dedicated, professional and friendly team we pride ourselves on delivering an exceptional legal service to our clients.</p>
  <div class="practice" style="top:654px;left:113px">
    <p>Our areas of practice include:</p>
    <ul>
      <li>Property Law</li><li>Conveyancing</li><li>Leases</li><li>Criminal Law</li><li>Family Law</li>
      <li>Litigation and Dispute Resolution</li><li>Company Law</li><li>Wills and Estates</li>
      <li>Powers of Attorney and Guardianship</li>
    </ul>
  </div>
  <footer class="footer">
    <div class="contact" style="top:12px">
      <div><svg viewBox="0 0 16 14" fill="currentColor"><path d="M8 0 0 6h2v8h5V9h2v5h5V6h2z"/></svg>3/82 Tarrow Street, Liverpool, NSW 2170</div>
      <div><svg viewBox="0 0 16 14" fill="currentColor" style="width:12px;margin-right:3px"><path d="M3 0h3l1 4-2 1q1 3 4 4l1-2 4 1v3q0 2-2 2Q2 12 1 2q0-2 2-2z"/></svg>(02) 9413 5862</div>
      <div><svg viewBox="0 0 16 14" fill="none" stroke="currentColor" stroke-width="1.4"><rect x="1" y="2" width="14" height="10"/><path d="m1 2 7 6 7-6"/></svg>info@pelburysolicitors-example.com.au</div>
    </div>
  </footer>
</section>

</body>
</html>
```